Simply Sugar Bloom Buisness Card

I would like a Buisness card and matching letterhead for my small but personal hobby/buisness.
Something elegant, professional and pretty.
I mainly do wedding cakes in our small rural area. But also do occasion cakes, cupcakes, cookies and catering events.
I am thinking something subtle, vintage, scrolls, lace, damask, nothing too wow or out there. But open to any suggestions.

Industry/Entity Type

Catering

Contact Information for Business Card

Simply Sugar Bloom
abn: 41 503 917 248
Marnie Holloway
Gayndah
t: 0491 352 806
e: sugarbloomcakes@pastrymail.example

Logo Text

Simply Sugar Bloom

Logo styles of interest
Wordmark Logo
Requirements
Must have
• Elegance and class
Should not have
• Should not have Hearts or Bows

```html
<!DOCTYPE html>
<html lang="en">
<head>
<meta charset="utf-8">
<title>Simply Sugar Bloom – Business Card</title>
<link rel="stylesheet" href="https://fonts.googleapis.com/css2?family=Playfair+Display:ital,wght@0,500;0,600;1,400&display=swap">
<style>
  :root {
    --page-bg: #f9ebf2;
    --card-bg: #fcf0f6;
    --card-edge: #e6d3dd;
    --brand-purple: #7b2d8e;
    --name-pink: #b8509a;
    --detail-pink: #c15aa4;
    --art-light: #d9a9c8;
    --art-dark: #7a2a5e;
  }
  * { margin: 0; padding: 0; box-sizing: border-box; }
  html, body {
    width: 1200px;
    height: 693px;
    overflow: hidden;
    background: var(--page-bg);
  }
  .card {
    position: absolute;
    left: 56px;
    top: 56px;
    width: 1088px;
    height: 582px;
    background: var(--card-bg);
    border: 2px solid var(--card-edge);
    box-shadow: inset 0 0 10px rgba(180, 140, 160, 0.25);
  }
  .brand-name {
    position: absolute;
    left: 44px;
    top: 80px;
    font-family: "Playfair Display", serif;
    font-weight: 500;
    font-size: 84px;
    line-height: 1;
    letter-spacing: -1px;
    color: var(--brand-purple);
    white-space: nowrap;
  }
  .owner-name {
    position: absolute;
    left: 92px;
    top: 250px;
    font-family: "Playfair Display", serif;
    font-weight: 600;
    font-size: 42px;
    line-height: 1;
    color: var(--name-pink);
    text-shadow: 1px 2px 3px rgba(120, 60, 100, 0.3);
    white-space: nowrap;
  }
  .contact-list {
    position: absolute;
    left: 98px;
    top: 314px;
    list-style: none;
    font-family: "Playfair Display", serif;
    font-style: italic;
    font-weight: 400;
    font-size: 35px;
    line-height: 52px;
    letter-spacing: -0.5px;
    color: var(--detail-pink);
    white-space: nowrap;
  }
  .cupcake-art {
    position: absolute;
    left: 830px;
    top: 113px;
    width: 226px;
    height: 350px;
  }
</style>
</head>
<body>
  <section class="card">
    <h1 class="brand-name">Simply Sugar Bloom</h1>
    <h2 class="owner-name">Marnie Holloway</h2>
    <ul class="contact-list">
      <li class="contact-phone">Phone: 0491 352 806</li>
      <li class="contact-email">E-mail: sugarbloomcakes@pastrymail.example</li>
      <li class="contact-abn">ABN: 41 503 917 248</li>
    </ul>
    <svg class="cupcake-art" viewBox="0 0 226 350" role="img" aria-label="Hand-drawn sketch of a cupcake with swirled icing topped by a cherry">
      <defs>
        <linearGradient id="cupcake-tone" x1="0" y1="0" x2="0" y2="1">
          <stop offset="0" stop-color="var(--art-light)"/>
          <stop offset="1" stop-color="var(--art-dark)" stop-opacity="0.55"/>
        </linearGradient>
      </defs>
      <rect x="0" y="0" width="226" height="350" rx="24" fill="url(#cupcake-tone)" opacity="0.6"/>
    </svg>
  </section>
</body>
</html>
```